Instagram Business Card For Comedian

Hi,

I'd like a 2-sided business card that kind mimics an Instagram page. I've attached screenshots with the copy and language that should be written on there.

I'd like it to be way more stylized and a bit more creative than what I did on Powerpoint. I just did a mockup so that you can have an idea. I'd like it to be designed and you to take a bit of creative imagery so that it doesn't look so static and monochromatic.

PLEASE BE CREATIVE WITH THESE DESIGNS. I DON'T WANT IT TO LOOK EXACTLY LIKE THE ATTACHED IMAGE OR EXACTLY LIKE AN INSTAGRAM PAGE. I want to use it as inspiration to create something that looks more sleek, and creative. I don't want the colors to just be boring gray, and blue. Have fun and spice it up a bit!

Check out my website LornaFabish.com to see the colors and fonts I use for my branding.

For the main photo: Here's a link with the hi-res photo: !https://www.filecrate-example.com/s/q8ktw3rmpadvhje/Lorna-Fabish-C71B2204.jpg?dl=0

For the thumbnail icon photo, you can use this: https://www.filecrate-example.com/s/xo5nvte2gwhrbsk/Lorna%20Fabish%20Tin%20Vale%20Headshot.jpg?dl=0

Use the Standard Business Card Template from Quillprint.com:
https://help.quillprint-example.com/hc/en-us/article_attachments/309827164/Standard_Size__US__Business_Cards_Portrait.jpg

Please let me know if you have any questions.
Updates

Industry/Entity Type

Business

Contact Information for Business Card

All of the text and copy has been provided on the attached jpg.

Colors
33a6d7
0255a3
aaaaaa
dbdbdb
1b1b1b

Requirements
Should not have
• A Hyperlink for the Email Addresses

```html
<!DOCTYPE html>
<html lang="en">
<head>
<meta charset="utf-8">
<title>LornaFab – Business Card</title>
<link rel="stylesheet" href="https://fonts.googleapis.com/css2?family=Roboto:wght@400;500&family=Roboto+Condensed:wght@400&display=swap">
<style>
  :root {
    --page: #8c8c8c;
    --card: #e9e9e9;
    --band: #d4d4d4;
    --brand-blue: #0a5ea8;
    --link-blue: #0255a3;
    --sky: #33a6d7;
    --ink: #1b1b1b;
    --muted: #6a6a6a;
    --rule: #aaaaaa;
  }
  * { box-sizing: border-box; margin: 0; padding: 0; }
  html, body { width: 1200px; height: 900px; overflow: hidden; }
  body {
    background: var(--page);
    font-family: "Roboto", Arial, sans-serif;
    color: var(--ink);
    position: relative;
  }
  .card {
    position: absolute;
    top: 225px;
    width: 266px;
    height: 447px;
    background: var(--card);
    border-radius: 16px;
    overflow: hidden;
  }
  .card--front { left: 286px; }
  .card--back { left: 639px; }

  /* Front: post */
  .post-avatar {
    position: absolute; left: 17px; top: 7px;
    width: 30px; height: 30px; border-radius: 50%;
    background: radial-gradient(circle at 50% 45%, #6b4a3a 0%, #2b1e18 70%);
  }
  .post-handle {
    position: absolute; left: 55px; top: 5px;
    font-size: 15px; line-height: 18px; color: #333;
  }
  .post-location {
    position: absolute; left: 55px; top: 23px;
    font-size: 12px; line-height: 15px; color: var(--link-blue);
  }
  .post-rule {
    position: absolute; left: 0; top: 44px; width: 100%; height: 2px;
    background: var(--link-blue);
  }
  .post-photo {
    position: absolute; left: 0; top: 46px; width: 100%; height: 269px;
    background: linear-gradient(160deg, #2a1d17 0%, #5c3a2a 40%, #8a5a40 60%, #2a1d17 100%);
  }
  .post-actions { position: absolute; left: 14px; top: 320px; }
  .post-progress {
    position: absolute; left: 14px; top: 341px; width: 239px; height: 1.5px;
    background: linear-gradient(to right, var(--link-blue) 0 89%, var(--rule) 89%);
  }
  .post-likes {
    position: absolute; left: 14px; top: 351px;
    display: flex; align-items: center; gap: 5px;
    font-size: 11px; color: var(--link-blue);
  }
  .post-caption {
    position: absolute; left: 14px; top: 369px; width: 245px;
    font-family: "Roboto Condensed", "Arial Narrow", sans-serif;
    font-size: 10px; line-height: 12.2px; color: var(--ink);
    white-space: nowrap;
  }

  /* Back: profile */
  .profile-header {
    position: absolute; left: 0; top: 0; width: 100%; height: 32px;
    background: var(--brand-blue); color: #fff;
    font-size: 14px; line-height: 32px; text-align: center; letter-spacing: .2px;
  }
  .band {
    position: absolute; left: 0; width: 100%; background: var(--band);
  }
  .band--top { top: 32px; height: 24px; }
  .band--about { top: 162px; height: 23px; }
  .band--more { top: 283px; height: 24px; }
  .band--foot { top: 425px; height: 22px; }
  .band-title {
    position: absolute; left: 18px; top: 0; line-height: 24px;
    font-size: 14px; color: var(--muted);
  }
  .band--about .band-title { line-height: 23px; }
  .profile-row {
    position: absolute; left: 41px; font-size: 10.4px; line-height: 12.5px;
    white-space: nowrap;
  }
  .profile-icon { position: absolute; left: 25px; }
  .profile-avatar {
    position: absolute; left: 198px; top: 44px;
    width: 44px; height: 44px; border-radius: 50%;
    background: radial-gradient(circle at 50% 45%, #6b4a3a 0%, #2b1e18 70%);
  }
  .profile-edit {
    position: absolute; left: 198px; width: 44px; top: 93px;
    text-align: center; font-size: 10.4px; color: var(--link-blue);
  }
  .about-text {
    position: absolute; left: 18px; top: 191px; width: 240px;
    font-size: 10px; line-height: 14.9px; white-space: nowrap;
  }
  .social {
    position: absolute; left: 22px; display: flex; align-items: center; gap: 15px;
    font-size: 10.4px;
  }
  .social-dot { width: 8px; height: 8px; border-radius: 50%; background: var(--link-blue); }
  .signoff {
    position: absolute; left: 0; width: 100%; top: 408px;
    text-align: center; font-size: 10.4px;
  }
</style>
</head>
<body>

<section class="card card--front" aria-label="Front of card">
  <div class="post-avatar" role="img" aria-label="Round thumbnail headshot"></div>
  <div class="post-handle">LornaFab</div>
  <div class="post-location">Brooklyn, New York</div>
  <div class="post-rule"></div>
  <div class="post-photo" role="img" aria-label="Main photo of Lorna Fabish covering her mouth with both hands, wearing gold nameplate rings reading Tin Vale"></div>

  <svg class="post-actions" width="70" height="16" viewBox="0 0 70 16" fill="none" stroke="#8a8a8a" stroke-width="1.2">
    <path d="M8 14 L2 8 A3.5 3.5 0 0 1 8 3.5 A3.5 3.5 0 0 1 14 8 Z"/>
    <path d="M29 13 A6 5.5 0 1 1 33 12 L35 14 Z"/>
    <path d="M46 14 V9 Q46 5 51 5 H56 M53 2 L56 5 L53 8"/>
  </svg>
  <svg style="position:absolute;left:247px;top:334px" width="4" height="4"><circle cx="2" cy="2" r="1.6" fill="#9a9a9a"/></svg>
  <div class="post-progress"></div>

  <div class="post-likes">
    <svg width="12" height="11" viewBox="0 0 12 11"><path d="M6 10.5 L1 5.5 A2.8 2.8 0 0 1 6 2 A2.8 2.8 0 0 1 11 5.5 Z" fill="#0255a3"/></svg>
    <span>32 Likes</span>
  </div>

  <p class="post-caption">lornafab Your faviorit comic's favorite comic. #ISAIDIT<br>#SOITSTRUE #FINDME #FOLLOWME #NOTTOMYHOUSE<br>#POSTABOUTMEUSINGTHESEHASHTAGS #LORNAFABISH<br>#LORNAFAB #IMSUCHABROOKLYNGIRL<br>#MAKENYUNSAFEAGAIN #BROOKLYNSTANDUPCOMEDY</p>
</section>

<section class="card card--back" aria-label="Back of card">
  <div class="profile-header">EDIT PROFILE</div>
  <div class="band band--top"></div>

  <svg class="profile-icon" style="top:64px" width="11" height="11" viewBox="0 0 11 11" fill="#0255a3">
    <circle cx="5.5" cy="3" r="2.6"/><path d="M0.5 11 Q0.5 6 5.5 6 Q10.5 6 10.5 11 Z"/>
  </svg>
  <div class="profile-row" style="top:64px">LORNA FABISH</div>

  <svg class="profile-icon" style="top:85px" width="11" height="10" viewBox="0 0 11 10" fill="none" stroke="#0255a3" stroke-width="1">
    <rect x="0.5" y="0.5" width="10" height="9"/><line x1="0.5" y1="3" x2="10.5" y2="3"/>
  </svg>
  <div class="profile-row" style="top:85px">www.lornafabish.com</div>

  <div class="profile-row" style="top:103px">For Booking Now:</div>
  <svg class="profile-icon" style="top:117px" width="11" height="9" viewBox="0 0 11 9" fill="none" stroke="#0255a3" stroke-width="1">
    <rect x="0.5" y="0.5" width="10" height="8"/><path d="M0.5 0.5 L5.5 5 L10.5 0.5"/>
  </svg>
  <div class="profile-row" style="top:116px">Dana@BrightlineTalent.com</div>
  <div class="profile-row" style="top:128px">Mira.Holt@ravenagency.com</div>

  <div class="profile-avatar" role="img" aria-label="Round profile headshot"></div>
  <div class="profile-edit">EDIT</div>

  <div class="band band--about"><span class="band-title">ABOUT</span></div>
  <p class="about-text">Stand Up Comedian. I Host. I Write. I Act. I Dance.<br>I Do Not. Sing Unless I'm in the Shower. I Accept<br>Tips. (Not on jokes but on Tipjarly.)<br>As seen on NBX, Laugh Channel, VJN, Real TV,<br>Verso and KTA.</p>

  <div class="band band--more"><span class="band-title">MORE INFO</span></div>
  <div class="social" style="top:325px"><span class="social-dot"></span><span>Friendspace.com/LornaFabish</span></div>
  <div class="social" style="top:348px"><span class="social-dot"></span><span>Chirper.com/Lornafab</span></div>
  <div class="social" style="top:369px"><span class="social-dot"></span><span>Snapgram.com/Lornafab</span></div>

  <div class="signoff">Let's Stay Connected!</div>
  <div class="band band--foot"></div>
</section>

</body>
</html>
```